Business Card Design for Orthopaedic Surgeon

This is a double-sided glossy business card. I prefer baby blue, teal, and green as color schemes. I have my logo already (many colors that you can choose from). I have photos and examples of my old card (very bland but has the information in it). I also have one that my assistant tried to design, but the writing is too small and I don't love the formatting. But it is close!
I would like my logo to be on the business card but I'm uploading my logo in many different colors so you can choose which one looks best based on the color scheme. I also uploaded many sized headshots so you can choose the best resolution one.

Additional information:
Correct business address:
4382 NW 58th Lane, Suite 305
Tamarac, FL 33417

Everything else on both business cards are accurate.

I actually need 2 different business cards generated. One that includes my cell phone number-- Personal cell: 585-314-9062 in addition to Office phone: (954) 316-4870 and Office Fax: 954-316-4881. Again, one card would have my personal cell and one wouldn't

Overall I just think the baby blue card (uploaded) is missing something on the front--of course it is also missing my office phone/fax/personal cell. I do want my website on the front too. Email: info@wellsorthocare.example

You can use your discretion about what goes on the front vs. what goes on the back to eliminated clutter.

Oh and on the back, I would like to list "Conditions Treated" (not specialties include). The list is:
Carpal Tunnel
Trigger Finger
Ganglion Cysts
Hand Tumors
Han & Wrist Arthritis
Hand, Wrist & Elbow Tendonitis
Fractures of the Hand, Wrist, Elbow and Humerus
Nerve Injuries of the Hand, Wrist & Elbow
Microsurgery
Wrist Arthroscopy
Endoscopic Surgery

Target Market(s)

Primary care doctors, Lawyers, patients

Industry/Entity Type

Medical

Contact Information for Business Card

Please see above in project description

Colors

Designer to choose colors to be used in the design.

Requirements
Must have
• -Correct office info, Board Certified Orthopaedic Hand & Upper Extremity Surgeon
Nice to have
• Something that is classy and wow!

```html
<!DOCTYPE html>
<html lang="en">
<head>
<meta charset="utf-8">
<title>Renata Wells, M.D. – Business Card</title>
<link rel="stylesheet" href="https://fonts.googleapis.com/css2?family=Montserrat:wght@400;500;600;700&display=swap">
<style>
  :root {
    --teal: #0b8480;
    --teal-deep: #076b68;
    --sky: #1f8fd3;
    --ink: #1b1b1b;
    --white: #ffffff;
    --gold: #d8b574;
    --backdrop: #efece6;
  }
  * { box-sizing: border-box; margin: 0; padding: 0; }
  html, body {
    width: 900px; height: 1200px; overflow: hidden;
    background: var(--backdrop);
    font-family: "Montserrat", Arial, sans-serif;
  }
  .canvas { position: relative; width: 900px; height: 1200px; }
  .card {
    position: absolute; left: 80px; width: 742px; height: 440px;
    border-radius: 28px; overflow: hidden;
    box-shadow: 0 6px 14px rgba(0,0,0,0.35);
  }
  .card-front { top: 132px; background: var(--white); }
  .card-back { top: 638px; background: var(--teal); }

  .front-wave { position: absolute; inset: 0; }
  .brand-disc {
    position: absolute; left: 28px; top: 10px; width: 240px; height: 240px;
    border-radius: 50%; background: var(--white);
    display: flex; align-items: center; justify-content: center;
  }
  .brand-name {
    font-weight: 600; font-size: 30px; color: var(--ink);
    letter-spacing: 1px; text-align: center; line-height: 1.15;
  }
  .doctor-name {
    position: absolute; left: 37px; top: 254px;
    font-size: 26px; font-weight: 700; color: var(--sky);
  }
  .doctor-title {
    position: absolute; left: 36px; top: 284px;
    font-size: 16px; font-weight: 400; color: var(--teal);
  }
  .contact-list {
    position: absolute; left: 38px; top: 326px; list-style: none;
  }
  .contact-list li {
    display: flex; align-items: center; gap: 12px;
    font-size: 16.5px; color: var(--ink); height: 23.5px;
  }
  .contact-list svg { width: 15px; height: 15px; fill: var(--teal); flex: none; }

  .portrait {
    position: absolute; left: 425px; top: 18px; width: 317px; height: 422px;
    background: linear-gradient(180deg, #e9ecef 0%, #cfc6c0 45%, #2a2526 100%);
  }
  .address-band { position: absolute; inset: 0; pointer-events: none; }
  .address {
    position: absolute; left: 465px; top: 370px;
    font-size: 16px; line-height: 21px; color: var(--white);
  }

  .conditions-title {
    position: absolute; left: 36px; top: 142px;
    font-size: 25px; font-weight: 600; color: var(--white);
  }
  .conditions-list {
    position: absolute; left: 55px; top: 193px;
    color: var(--white); font-size: 16.5px; line-height: 19.6px;
  }
  .back-brand {
    position: absolute; left: 452px; top: 46px; width: 214px; height: 214px;
    border-radius: 50%; border: 3px solid var(--gold);
    display: flex; align-items: center; justify-content: center;
  }
  .back-brand .brand-name { color: var(--gold); }
</style>
</head>
<body>
<main class="canvas">

  <section class="card card-front" aria-label="Card front">
    <svg class="front-wave" viewBox="0 0 742 440" aria-hidden="true">
      <path fill="var(--teal)" d="M0,0 H742 V135 C650,90 560,90 470,110 C380,130 300,215 200,215 C120,215 60,185 0,175 Z"/>
    </svg>

    <div class="portrait" role="img" aria-label="Headshot portrait of the doctor in a dark blazer"></div>

    <svg class="address-band" viewBox="0 0 742 440" aria-hidden="true">
      <polygon fill="var(--teal)" points="398,416 425,356 742,356 742,416"/>
    </svg>
    <p class="address">4382 NW 58th Lane, Suite 305<br>Tamarac, FL 33417</p>

    <div class="brand-disc">
      <span class="brand-name">Wells<br>Hand</span>
    </div>

    <h1 class="doctor-name">Renata Wells, M.D.</h1>
    <p class="doctor-title">Hand and upper extremity specialist</p>

    <ul class="contact-list">
      <li>
        <svg viewBox="0 0 16 16"><path d="M2 6c0-2 2.5-3 6-3s6 1 6 3v1h-3V5.5H5V7H2zM4 8h8l2 5H2z"/></svg>
        (954) 316-4870
      </li>
      <li>
        <svg viewBox="0 0 16 16"><path d="M4.5 1h7a1 1 0 0 1 1 1v12a1 1 0 0 1-1 1h-7a1 1 0 0 1-1-1V2a1 1 0 0 1 1-1zm.5 2v9h6V3zm3 10a.8.8 0 1 0 0 .1z"/></svg>
        585-314-9062
      </li>
      <li>
        <svg viewBox="0 0 16 16"><path d="M5 1h6v4H5zM1 6h14v8H1zm3 2v2h2V8zm4 0v2h4V8z"/></svg>
        954-316-4881
      </li>
      <li>
        <svg viewBox="0 0 16 16"><path d="M1 4h14v9H1zm1 1 6 4.5L14 5z"/></svg>
        info@wellsorthocare.example
      </li>
    </ul>
  </section>

  <section class="card card-back" aria-label="Card back">
    <h2 class="conditions-title">Conditions Treated</h2>
    <ul class="conditions-list">
      <li>Carpal Tunnel</li>
      <li>Trigger Finger</li>
      <li>Ganglion Cysts</li>
      <li>Hand Tumors</li>
      <li>Han &amp; Wrist Arthritis</li>
      <li>Hand, Wrist &amp; Elbow Tendonitis</li>
      <li>Fractures of the Hand, Wrist, Elbow and Humerus</li>
      <li>Nerve Injuries of the Hand, Wrist &amp; Elbow</li>
      <li>Microsurgery</li>
      <li>Wrist Arthroscopy</li>
      <li>Endoscopic Surgery</li>
    </ul>
    <div class="back-brand">
      <span class="brand-name">Wells<br>Hand</span>
    </div>
  </section>

</main>
</body>
</html>
```